***Design a Nutritional Supplement Label for Bright Harvest!***

I have an existing label, I want to keep the logo but change the rest of the design. I am open to different creative ideas, but it needs to look appropriate for the shelves at Bright Harvest. This means it needs to look professional and premium, without being sterile and boring. I feel like my current label looks a little 1990s. You can play with the colors, font and design elements, while keeping the logo, descriptive text and the same layout. Feel free to take some bold chances. (You cannot change the font in the supplement facts section)

Font styles to use
Sans Serif

Colors

Designer to choose colors to be used in the design.

Requirements
Must have
• Keep the same text and layout. Keep the "Muscle Haven" logo as-is. DO NOT CHANGE THE LOGO!!

```html
<!DOCTYPE html>
<html lang="en">
<head>
<meta charset="utf-8">
<title>Muscle Haven – Supplement Label</title>
<link rel="stylesheet" href="https://fonts.googleapis.com/css2?family=Nunito+Sans:wght@700;800;900&display=swap">
<style>
  :root {
    --backdrop: #1f5e91;
    --label-light: #f4f4f4;
    --label-shade: #e3e3e3;
    --brand-blue: #2a9fd8;
    --sweep-blue: #1e8fd0;
    --sweep-green: #86bf3c;
    --panel-grey: #d4d6d8;
    --panel-grey-light: #eceded;
    --pill-blue: #3fb0e6;
    --pill-text: #e9f6fd;
    --ink: #2b2b2b;
  }
  * { margin: 0; padding: 0; box-sizing: border-box; }
  html, body {
    width: 1200px;
    height: 810px;
    overflow: hidden;
    background: var(--backdrop);
  }
  .canvas {
    position: relative;
    width: 1200px;
    height: 810px;
    background: var(--backdrop);
  }
  .label {
    position: absolute;
    left: 298px;
    top: 25px;
    width: 604px;
    height: 760px;
    display: block;
    box-shadow: 0 10px 30px rgba(0, 0, 0, 0.25);
  }
  .label text { font-family: "Nunito Sans", sans-serif; }
  .brand-name {
    fill: var(--brand-blue);
    font-weight: 800;
  }
  .pill-text {
    fill: var(--pill-text);
    font-weight: 700;
    font-size: 15px;
    letter-spacing: 0.5px;
  }
  .count {
    fill: var(--ink);
    font-weight: 800;
    font-size: 24px;
  }
  .category {
    fill: var(--ink);
    font-weight: 800;
    font-size: 16px;
    letter-spacing: 1.2px;
  }
</style>
</head>
<body>
<main class="canvas">
  <svg class="label" viewBox="0 0 445 560" xmlns="http://www.w3.org/2000/svg" aria-label="Muscle Haven dietary supplement label">
    <defs>
      <linearGradient id="label-bg" x1="0" y1="0" x2="1" y2="0">
        <stop offset="0" stop-color="var(--label-shade)"/>
        <stop offset="0.5" stop-color="var(--label-light)"/>
        <stop offset="1" stop-color="var(--label-shade)"/>
      </linearGradient>
      <linearGradient id="panel-bg" x1="0" y1="0" x2="0" y2="1">
        <stop offset="0" stop-color="var(--panel-grey)"/>
        <stop offset="1" stop-color="var(--panel-grey-light)"/>
      </linearGradient>
      <linearGradient id="sweep-bg" x1="0" y1="0" x2="0" y2="1">
        <stop offset="0" stop-color="var(--sweep-blue)"/>
        <stop offset="1" stop-color="var(--sweep-green)"/>
      </linearGradient>
      <radialGradient id="photo-bg" cx="0.55" cy="0.45" r="0.7">
        <stop offset="0" stop-color="#c9c9c9"/>
        <stop offset="0.35" stop-color="#d9a6a0"/>
        <stop offset="0.6" stop-color="#bdbdbd"/>
        <stop offset="1" stop-color="#d6d7d8"/>
      </radialGradient>
      <clipPath id="label-clip">
        <rect x="0" y="0" width="445" height="560"/>
      </clipPath>
    </defs>

    <g clip-path="url(#label-clip)">
      <rect class="label-base" x="0" y="0" width="445" height="560" fill="url(#label-bg)"/>

      <path class="lower-panel" d="M0,300 C150,305 300,350 445,396 L445,560 L0,560 Z" fill="url(#panel-bg)"/>

      <path class="product-photo" role="img" aria-label="Photo of a person holding a cramping upper arm"
            d="M205,560 C195,500 200,450 240,420 C290,385 360,370 445,380 L445,560 Z"
            fill="url(#photo-bg)" opacity="0.85"/>

      <path class="decor-sweep" role="img" aria-label="Decorative sweeping band in blue and green"
            d="M0,208 C120,210 260,250 445,300 L445,396 C300,350 150,302 0,298 Z"
            fill="url(#sweep-bg)"/>

      <text class="brand-name" x="222" y="132" text-anchor="middle" font-size="72">MUSCLE</text>
      <text class="brand-name" x="233" y="192" text-anchor="middle" font-size="40" letter-spacing="22">HAVEN</text>

      <g class="claim-pill" transform="translate(52,438) rotate(-40)">
        <rect x="-110" y="-19" width="220" height="38" rx="19" fill="var(--pill-blue)"/>
        <text class="pill-text" x="-8" y="5" text-anchor="middle">ABSORPTION</text>
      </g>
      <g class="claim-pill" transform="translate(92,482) rotate(-40)">
        <rect x="-100" y="-19" width="200" height="38" rx="19" fill="var(--pill-blue)"/>
        <text class="pill-text" x="0" y="5" text-anchor="middle">FAST ACTING</text>
      </g>

      <text class="count" x="212" y="521" text-anchor="middle">180 CAPSULES</text>
      <text class="category" x="212" y="549" text-anchor="middle">DIETARY SUPPLEMENT</text>
    </g>
  </svg>
</main>
</body>
</html>
```